Builder of high-end, expensive tables and other furniture

Build a website that represents what we do. I want a luxury feel that appeals to those who can afford our products. We build very high end tables and other furniture using trees that have fallen or are standing dead. We never cut living trees. Trees are harvested, milled, and kiln dried. Then that lumber is meticulously turned into fine furniture using the best equipment. Our furniture prices range from $1,000-$20,000.

Trying to figure out how to raise my spend.

```html
<!DOCTYPE html>
<html lang="en">
<head>
<meta charset="utf-8">
<title>Heritage Timberworks</title>
<link href="https://fonts.googleapis.com/css2?family=Cinzel:wght@600;700&family=Lato:ital,wght@0,400;0,700;1,400&family=Montserrat:wght@600&display=swap" rel="stylesheet">
<style>
:root{
  --orange:#ef6c1f;
  --blue:#1f63b8;
  --blue-deep:#1553a3;
  --ink:#111;
  --text:#333;
  --muted:#666;
  --panel:#f4f4f4;
  --card:#f5f5f5;
  --blush:#f7d8c6;
  --black:#000;
  --white:#fff;
}
*{box-sizing:border-box;margin:0;padding:0}
html,body{width:1200px;height:3452px;overflow:hidden}
body{position:relative;background:var(--white);font-family:'Lato',sans-serif;color:var(--text)}
.abs{position:absolute}
.heading{font-family:'Cinzel',serif;font-weight:700;color:var(--ink);letter-spacing:.5px}
.btn{position:absolute;display:flex;align-items:center;justify-content:center;background:var(--orange);color:var(--white);border-radius:30px;font-family:'Cinzel',serif;font-weight:700;font-size:15px;letter-spacing:.5px}

/* header */
.site-header{position:absolute;left:0;top:0;width:1200px;height:91px;background:var(--white)}
.brand{position:absolute;left:113px;top:26px;font-family:'Lato',sans-serif;font-weight:700;font-size:32px;color:var(--blue)}
.nav{position:absolute;top:36px;left:593px;display:flex;gap:0;font-size:14px;color:#222}
.nav span{position:absolute;white-space:nowrap}

/* hero */
.hero{position:absolute;left:0;top:91px;width:1200px;height:563px;background:linear-gradient(100deg,#1b5fb3 0%,#2b72c6 50%,#1a5aae 100%)}
.hero-title{position:absolute;left:111px;top:127px;font-size:56px;line-height:72px;color:var(--white)}
.hero-text{position:absolute;left:111px;top:272px;width:460px;font-size:16px;line-height:26px;color:var(--white)}
.hero-photo{position:absolute;left:603px;top:150px;width:490px;height:348px;border-radius:8px;background:radial-gradient(ellipse at 50% 45%,#a0602d 0%,#7a4420 45%,rgba(90,50,25,0) 72%)}

/* process */
.process{position:absolute;left:0;top:654px;width:1200px;height:417px;background:linear-gradient(180deg,#ece9e4 0%,#f6f4f1 55%,#fff 100%)}
.section-title{position:absolute;left:0;width:1200px;text-align:center;font-size:31px}
.step{position:absolute;width:300px;text-align:center}
.step-blob{position:absolute;width:92px;height:88px;background:var(--blush);border-radius:48% 52% 44% 56%/55% 45% 55% 45%}
.step h3{font-family:'Cinzel',serif;font-weight:700;font-size:20px;color:var(--ink)}
.step p{margin-top:14px;font-size:13.5px;line-height:26px;color:var(--text)}

/* about */
.about{position:absolute;left:3px;top:1145px;width:1195px;height:586px;background:var(--panel)}
.about-photo{position:absolute;left:114px;top:1244px;width:452px;height:390px;border-radius:26px;background:linear-gradient(135deg,#3a2a20 0%,#6b4a32 45%,#b07a4a 70%,#2d2520 100%)}
.about-title{position:absolute;left:601px;top:1260px;font-size:34px}
.about-text{position:absolute;left:601px;width:500px;font-size:15px;line-height:25.7px;color:var(--text)}

/* products */
.product{position:absolute;top:1979px;width:300px;height:253px;background:var(--card);border-radius:40px;text-align:center}
.product-photo{position:absolute;border-radius:8px}
.product h3{position:absolute;left:0;top:165px;width:300px;font-family:'Cinzel',serif;font-weight:700;font-size:26px;color:var(--ink)}
.product .price{position:absolute;left:0;top:205px;width:300px;font-family:'Montserrat',sans-serif;font-weight:600;font-size:15px;color:var(--orange)}

/* testimonials */
.testimonials{position:absolute;left:0;top:2343px;width:1200px;height:652px;background:linear-gradient(180deg,#f1f1f1 0%,#f7f7f7 25%,#ececec 45%,#f6f6f6 100%)}
.quote-badge{position:absolute;left:565px;top:2409px;width:62px;height:62px;border-radius:50%;background:var(--orange)}
.t-card{position:absolute;top:2638px;background:var(--white);border-radius:6px;padding:24px 28px;box-shadow:0 6px 18px rgba(0,0,0,.05)}
.t-card p{font-style:italic;font-size:13.2px;line-height:26px;color:#444}
.t-card .who{margin-top:10px;font-family:'Cinzel',serif;font-weight:700;font-size:16px;color:var(--orange);letter-spacing:.5px}
.t-card.faded{opacity:.45}
.dot{position:absolute;top:2896px;width:10px;height:10px;border-radius:50%;background:#bbb}

/* footer */
.site-footer{position:absolute;left:0;top:2995px;width:1200px;height:457px;background:var(--black);color:var(--white)}
.footer-brand{position:absolute;left:114px;top:3082px;font-family:'Lato',sans-serif;font-weight:700;font-size:40px;color:var(--orange)}
.footer-about{position:absolute;left:114px;top:3180px;width:350px;font-size:14.5px;line-height:26px}
.f-col{position:absolute;top:3060px}
.f-col h4{font-family:'Cinzel',serif;font-weight:700;font-size:19px;letter-spacing:.3px}
.f-col .rule{width:38px;height:3px;background:var(--white);margin-top:9px}
.f-col ul{list-style:none;margin-top:16px}
.f-col li{font-size:14.5px;line-height:30px}
.f-col.small li{font-size:13px}
.footer-rule{position:absolute;left:107px;top:3347px;width:975px;height:1px;background:#333}
.copyright{position:absolute;left:0;top:3380px;width:1200px;text-align:center;font-size:14.5px}
</style>
</head>
<body>

<header class="site-header">
  <div class="brand">Heritage Timberworks</div>
  <nav class="nav">
    <span style="left:0">Home</span>
    <span style="left:71px">About Us</span>
    <span style="left:162px">Our Products</span>
    <span style="left:279px">Blog</span>
    <span style="left:337px">Testimonial</span>
    <span style="left:447px">Contact</span>
  </nav>
</header>

<section class="hero">
  <h1 class="heading hero-title">WELCOME TO<br>HERITAGE TABLES</h1>
  <p class="hero-text">Lorem ipsum dolor sit amet, consectetur adipiscing elit, sed do eiusmod tempor incididunt ut labore et dolore</p>
  <div class="hero-photo" role="img" aria-label="Round wooden dining table with four folding chairs"></div>
</section>
<div class="btn" style="left:110px;top:439px;width:178px;height:54px">GET STARTED</div>

<section class="process" role="presentation"></section>
<div class="section-title heading" style="top:730px">OUR PROCESS</div>
<svg class="abs" style="left:310px;top:830px" width="560" height="110" viewBox="0 0 560 110" aria-hidden="true">
  <path d="M20 48 C70 60 100 58 120 50 C150 30 145 -5 118 8 C90 25 100 75 160 90 C195 98 225 70 240 58" fill="none" stroke="#111" stroke-width="3" stroke-dasharray="10 9"/>
  <path d="M330 32 C400 20 440 80 480 95 C520 105 545 90 560 78" fill="none" stroke="#111" stroke-width="3" stroke-dasharray="10 9"/>
</svg>
<div class="step-blob" style="left:230px;top:832px"></div>
<svg class="abs" style="left:256px;top:858px" width="40" height="36" viewBox="0 0 40 36" fill="none" stroke="#1f63b8" stroke-width="2" aria-hidden="true"><path d="M2 32h36M8 32V16M14 32V8l6 4v20M26 32V12l4-4v24M34 32V18"/></svg>
<div class="step-blob" style="left:553px;top:832px"></div>
<svg class="abs" style="left:562px;top:862px" width="52" height="30" viewBox="0 0 52 30" fill="none" stroke="#1f63b8" stroke-width="2" aria-hidden="true"><rect x="4" y="6" width="30" height="16" rx="2"/><path d="M8 10v8M13 10v8M18 10v8M23 10v8M28 10v8M34 10h8v8h-8M42 12h6v4h-6M2 26h48"/></svg>
<div class="step-blob" style="left:863px;top:832px"></div>
<svg class="abs" style="left:889px;top:855px" width="38" height="40" viewBox="0 0 38 40" fill="none" stroke="#1f63b8" stroke-width="2" aria-hidden="true"><rect x="2" y="2" width="34" height="36" rx="2"/><rect x="7" y="12" width="24" height="22"/><path d="M19 30c-4 0-6-3-4-7 1 2 2 2 2 0 0-3 2-4 4-6 0 4 4 5 3 9-1 3-3 4-5 4z"/><path d="M7 7h8"/></svg>
<div class="step" style="left:133px;top:938px"><h3>Trees Are Harvested</h3><p>Lorem ipsum dolor sit amet, consec-<br>tetur adipiscing elit</p></div>
<div class="step" style="left:450px;top:938px"><h3>Milled</h3><p>Lorem ipsum dolor sit amet, consec-<br>tetur adipiscing elit</p></div>
<div class="step" style="left:767px;top:938px"><h3>Kiln Dried</h3><p>Lorem ipsum dolor sit amet, consec-<br>tetur adipiscing elit</p></div>

<section class="about"></section>
<div class="about-photo" role="img" aria-label="Craftsman inspecting a wooden frame in the workshop"></div>
<h2 class="heading about-title">ABOUT HERITAGE TABLES</h2>
<p class="about-text" style="top:1321px">Lorem ipsum dolor sit amet, consectetur adipiscing elit, sed do eiusmod tempor incididunt ut labore et dolore magna aliqua. Quis ipsum sus-pendisse ultrices gravida. Risus commodo viverra maecenas accumsan lacus vel facilisis.</p>
<p class="about-text" style="top:1450px">Lorem ipsum dolor sit amet, consectetur adipiscing elit, sed do eiusmod tempor incididunt ut labore et dolore magna aliqua. Quis ipsum sus-pendisse ultrices gravida. Risus commodo viverra maecenas accumsan</p>
<div class="btn" style="left:598px;top:1556px;width:199px;height:55px">LEARN MORE</div>

<div class="section-title heading" style="top:1822px">OUR PRODUCTS</div>
<div class="product" style="left:122px"><h3>COFFEE TABLE</h3><div class="price">$4,000</div></div>
<div class="product" style="left:451px"><h3>ROUND TABLE</h3><div class="price">$4,000</div></div>
<div class="product" style="left:779px"><h3>WOODEN TABLE</h3><div class="price">$4,000</div></div>
<div class="product-photo abs" style="left:140px;top:1950px;width:268px;height:104px;background:linear-gradient(180deg,#d9a56a,#b9844e)" role="img" aria-label="Light oak coffee table"></div>
<div class="product-photo abs" style="left:518px;top:1928px;width:178px;height:188px;background:radial-gradient(ellipse at 50% 18%,#c57a4c 0%,#a45e35 40%,rgba(164,94,53,0) 70%)" role="img" aria-label="Round table with splayed legs"></div>
<div class="product-photo abs" style="left:838px;top:1928px;width:174px;height:192px;background:linear-gradient(180deg,#c9a77a 0%,#b89266 35%,rgba(190,150,100,.35) 100%)" role="img" aria-label="Wooden side table with drawer"></div>

<section class="testimonials"></section>
<div class="quote-badge"></div>
<svg class="abs" style="left:582px;top:2428px" width="28" height="24" viewBox="0 0 28 24" fill="#fff" aria-hidden="true"><path d="M2 22c0-9 3-15 10-19l1 3c-3 2-5 5-5 8h4v8zM16 22c0-9 3-15 10-19l1 3c-3 2-5 5-5 8h4v8z"/></svg>
<div class="section-title heading" style="top:2490px;font-size:36px">CLIENT TESTIMONIALS</div>
<p class="abs" style="left:270px;top:2545px;width:660px;text-align:center;font-size:14px;line-height:26px;color:#444">Lorem ipsum dolor sit amet, consectetur adipiscing elit, sed do eiusmod tempor incididunt ut labore et dolore magna aliqua. Quis ipsum suspendisse ultrices gravida.</p>
<div class="t-card faded" style="left:-306px;width:408px;height:195px;text-align:right;overflow:hidden"><p>Lorem ipsum dolor sit amet, adipiscing elit, sed do eiusmod tempor incididunt dolore magna aliqua. Risus com-modo viverra facilisis.</p></div>
<div class="t-card" style="left:122px;width:408px;height:195px"><p>Lorem ipsum dolor sit amet, consectetur adipiscing elit, sed do eiusmod tempor incididunt ut labore et dolore magna aliqua. Quis ipsum suspendisse ultrices gravida. Risus com-modo viverra maecenas accumsan lacus vel facilisis.</p><div class="who">Mara Quill</div></div>
<div class="t-card" style="left:549px;width:408px;height:151px"><p>Lorem ipsum dolor sit amet, consectetur adipiscing elit, sed do eiusmod tempor incididunt ut labore et</p><div class="who" style="margin-top:14px">Dorian Fenwick</div></div>
<div class="t-card faded" style="left:977px;width:408px;height:195px;overflow:hidden"><p>Lorem ipsum dolor sit amet, consectetur adipiscing elit, sed do eiusmod tempor incididunt ut labore et dolore magna aliqua. Quis ipsum suspendisse ultrices gravida. Risus com-modo viverra maecenas accumsan</p><div class="who">Dorian Fenwick</div></div>
<div class="dot" style="left:574px;background:var(--orange)"></div>
<div class="dot" style="left:590px"></div>
<div class="dot" style="left:606px"></div>

<footer class="site-footer"></footer>
<div class="footer-brand">Heritage Timberworks</div>
<p class="footer-about">Lorem ipsum dolor sit amet, consectetur adipiscing elit, sed do eiusmod tempor incididunt ut labore et dolore magna aliqua.</p>
<div class="f-col small" style="left:560px;color:#fff"><h4>QUICK LINKS</h4><div class="rule"></div><ul><li>Home</li><li>About Us</li><li>Our Products</li><li>Blog</li><li>Testimonial</li><li>Contact</li></ul></div>
<div class="f-col" style="left:759px;color:#fff"><h4>HELP LINKS</h4><div class="rule"></div><ul><li>Terms &amp; conditions</li><li>Privacy Policy</li><li>About Us</li><li>Support</li></ul></div>
<div class="f-col" style="left:963px;color:#fff"><h4>CONTACT US</h4><div class="rule"></div><ul><li>Grainbook</li><li>Chirpline</li><li>Linkwork</li></ul></div>
<div class="footer-rule"></div>
<p class="copyright" style="color:#fff">©Copyrights 2023 Heritage Timberworks. &nbsp;| &nbsp;&nbsp;All Rights Reserved</p>

</body>
</html>
```